Brindle Logistics Business Card Design

We are a trucking and warehousing company. We run freight in the US manly from the Pacific NW to TX and back up the the PNW. We also do warehousing where we store, move, and distribute freight. Looking for a clean and modern design of business card. We would like to look rich and elegant. Attached is our logo.

Industry/Entity Type

Trucking Company

Contact Information for Business Card

Looking for a clean and modern design of business card. We would like to look rich and elegant.

Font styles to use
Sans Serif

Colors

Designer to choose colors to be used in the design.

Requirements
Must have
• logo but it should not dominate the card
Should not have
• logo should not dominate the card

```html
<!DOCTYPE html>
<html lang="en">
<head>
<meta charset="utf-8">
<title>Brindle Logistics Business Card</title>
<link href="https://fonts.googleapis.com/css2?family=Open+Sans:wght@300;400;600&family=Roboto+Condensed:wght@700&display=swap" rel="stylesheet">
<style>
  :root {
    --bg: #e9e7e4;
    --card: #ffffff;
    --ink: #3a3d42;
    --muted: #8a8d92;
    --navy: #1f3552;
    --blue: #1d6fb8;
    --rule: #54585e;
    --photo-a: #efe6e6;
    --photo-b: #e6cccc;
  }
  * { box-sizing: border-box; margin: 0; padding: 0; }
  html, body { width: 1200px; height: 1200px; overflow: hidden; }
  body {
    background: var(--bg);
    font-family: "Open Sans", sans-serif;
    color: var(--ink);
    position: relative;
  }
  .card {
    position: absolute;
    left: 150px;
    width: 900px;
    height: 514px;
    border-radius: 36px;
    background: var(--card);
    overflow: hidden;
    box-shadow: 0 10px 30px rgba(0,0,0,0.15);
  }
  .card--front { top: 62px; }
  .card--back { top: 624px; }

  .photo {
    position: absolute;
    left: 0; top: 0;
    width: 100%; height: 300px;
    background: radial-gradient(ellipse at 62% 45%, var(--photo-b) 0%, var(--photo-a) 40%, #f6f6f6 75%, #ffffff 100%);
  }
  .divider {
    position: absolute;
    left: 0; top: 300px;
    width: 100%; height: 3px;
    background: var(--rule);
  }
  .name-bar {
    position: absolute;
    left: 0; top: 200px;
    width: 14px; height: 100px;
    background: var(--navy);
  }
  .identity {
    position: absolute;
    left: 46px; top: 178px;
  }
  .name {
    font-family: "Roboto Condensed", sans-serif;
    font-weight: 700;
    font-size: 70px;
    line-height: 1;
    letter-spacing: 0.5px;
    color: var(--ink);
    text-transform: uppercase;
  }
  .role {
    font-weight: 300;
    font-size: 36px;
    line-height: 1;
    color: var(--muted);
    text-align: right;
    margin-top: 2px;
  }
  .contacts {
    position: absolute;
    top: 330px;
    font-size: 27px;
    line-height: 1.45;
    color: var(--ink);
    list-style: none;
  }
  .contacts--phones { left: 110px; }
  .contacts--web { left: 440px; }
  .contacts li { display: flex; align-items: flex-start; gap: 14px; }
  .icon { width: 28px; height: 28px; flex: none; margin-top: 8px; fill: var(--navy); }
  .address { line-height: 1.2; margin-top: 6px; }

  .edge {
    position: absolute;
    right: 0; top: 0;
    width: 26px; height: 100%;
    background: var(--navy);
  }
  .brand {
    position: absolute;
    left: 50%; top: 50%;
    transform: translate(-50%, -50%);
    display: flex;
    align-items: center;
    gap: 22px;
  }
  .brand-mark {
    width: 54px; height: 54px;
    border-radius: 50%;
    background: var(--blue);
  }
  .brand-name {
    font-weight: 600;
    font-size: 54px;
    color: var(--ink);
    letter-spacing: 1px;
  }
</style>
</head>
<body>
  <section class="card card--front">
    <div class="photo" role="img" aria-label="Faded photo of a red box truck and a forklift"></div>
    <div class="divider"></div>
    <div class="name-bar"></div>
    <div class="identity">
      <h1 class="name">Dale Corwin</h1>
      <p class="role">President</p>
    </div>
    <ul class="contacts contacts--phones">
      <li><svg class="icon" viewBox="0 0 24 24"><path d="M6.6 2.5c.6-.3 1.3 0 1.6.6l1.6 3.4c.3.6.1 1.3-.4 1.7L8 9.3c1 2.4 3.2 4.7 5.7 5.8l1.2-1.5c.4-.5 1.1-.7 1.7-.4l3.4 1.6c.6.3.9 1 .6 1.6l-.9 2.6c-.3.8-1.1 1.3-2 1.2C9.8 19.3 4.7 14.2 3.8 6.4c-.1-.9.4-1.7 1.2-2z"/></svg>(000) 000-0000,</li>
      <li><svg class="icon" viewBox="0 0 24 24"><path d="M6.6 2.5c.6-.3 1.3 0 1.6.6l1.6 3.4c.3.6.1 1.3-.4 1.7L8 9.3c1 2.4 3.2 4.7 5.7 5.8l1.2-1.5c.4-.5 1.1-.7 1.7-.4l3.4 1.6c.6.3.9 1 .6 1.6l-.9 2.6c-.3.8-1.1 1.3-2 1.2C9.8 19.3 4.7 14.2 3.8 6.4c-.1-.9.4-1.7 1.2-2z"/></svg>(000) 000-0000,</li>
      <li><svg class="icon" viewBox="0 0 24 24"><path d="M7 1h10a2 2 0 0 1 2 2v18a2 2 0 0 1-2 2H7a2 2 0 0 1-2-2V3a2 2 0 0 1 2-2zm0 3v14h10V4zm5 15.5a1 1 0 1 0 0 2 1 1 0 0 0 0-2z"/></svg>(000) 000-0000,</li>
    </ul>
    <ul class="contacts contacts--web">
      <li><svg class="icon" viewBox="0 0 24 24"><path d="M2 5h20v14H2zm2.4 2 7.6 6 7.6-6zM4 8.6V17h16V8.6l-8 6.3z"/></svg>hello@brindlefreight.com</li>
      <li><svg class="icon" viewBox="0 0 24 24"><path d="M12 2a10 10 0 1 0 0 20 10 10 0 0 0 0-20zm-1 3.2c-1 1-1.6 2.5-3.6 3-1 .3-.6 1.7.4 2.3 1.5.8 1 2.6 2.4 3.4.9.5.4 2.6 1.3 3.8C7.5 17 5 14.3 5 12a7 7 0 0 1 6-6.8zm3.3.4A7 7 0 0 1 19 12c0 1.2-.3 2.3-.8 3.3-.8-1-2-.8-2.5-2-.4-1.1.8-2-.2-3-1-1-2.4-.2-2.7-1.4-.2-1 1.3-1.5 1.5-3.3z"/></svg>www.brindlefreight.com</li>
      <li><svg class="icon" viewBox="0 0 24 24"><path d="M12 1a8 8 0 0 0-8 8c0 6 8 14 8 14s8-8 8-14a8 8 0 0 0-8-8zm0 4.5a3.5 3.5 0 1 1 0 7 3.5 3.5 0 0 1 0-7z"/></svg><span class="address">418 Harbor Row, 3rd Floor,<br>Tacoma, WA 98400</span></li>
    </ul>
  </section>

  <section class="card card--back">
    <div class="edge"></div>
    <div class="brand">
      <span class="brand-mark"></span>
      <span class="brand-name">Brindle Logistics</span>
    </div>
  </section>
</body>
</html>
```